North Fern Holdings Business Card

A business card design to accompany the logo design you completed on Artisan Hive. We are open to your proposals. I did add one idea below that might work, but we aren't married to the idea. The company is a real estate services company. Clientele are typically high net worth individuals, executive level employment or owners of their own company, 30-60 years old.

Our 1 (bad?) idea: double sided card; One side landscape with logo and word mark. Other side Portrait with the logo only (oversize watermark maybe?). Somewhere add text of Name (Marcus Pellington), Title (Principal), phone # (949-555-0173) and email address (marcus@northfernhq.com). There would be a second design with my wife's name, number and email in place of mine.

Again totally open to ideas here.

Industry/Entity Type

Real Estate

```html
<!DOCTYPE html>
<html lang="en">
<head>
<meta charset="utf-8">
<title>North Fern Holdings — Business Card</title>
<link rel="stylesheet" href="https://fonts.googleapis.com/css2?family=Cinzel:wght@400&family=Marcellus+SC&family=Arimo:ital@0;1&display=swap">
<style>
  :root {
    --fern: #64965a;
    --fern-light: #9cbf8e;
    --paper: #ffffff;
    --backdrop: #ecebe7;
    --ink-light: #ffffff;
    --shadow: rgba(0, 0, 0, 0.12);
  }
  * { margin: 0; padding: 0; box-sizing: border-box; }
  html, body {
    width: 900px;
    height: 1200px;
    overflow: hidden;
    background: var(--backdrop);
  }
  .canvas {
    position: relative;
    width: 900px;
    height: 1200px;
  }
  .card {
    position: absolute;
    box-shadow: 0 6px 18px var(--shadow);
    overflow: hidden;
  }

  /* Front: landscape wordmark side */
  .card-front {
    left: 135px;
    top: 90px;
    width: 630px;
    height: 378px;
    background: var(--paper);
    display: flex;
    align-items: center;
    justify-content: center;
    gap: 34px;
  }
  .brand-dot {
    width: 74px;
    height: 74px;
    border-radius: 50%;
    background: var(--fern);
    flex: none;
  }
  .wordmark {
    font-family: "Cinzel", serif;
    font-weight: 400;
    color: var(--fern);
    line-height: 1.05;
  }
  .wordmark-main {
    display: block;
    font-size: 54px;
    letter-spacing: 1px;
  }
  .wordmark-sub {
    display: block;
    font-size: 34px;
    letter-spacing: 6px;
    padding-left: 62px;
  }

  /* Back: portrait contact side */
  .card-back {
    left: 261px;
    top: 520px;
    width: 378px;
    height: 630px;
    background: var(--fern);
  }
  .watermark {
    position: absolute;
    right: -150px;
    top: -40px;
    width: 440px;
    height: 440px;
  }
  .contact {
    position: absolute;
    left: 34px;
    top: 504px;
    color: var(--ink-light);
  }
  .contact-name {
    font-family: "Marcellus SC", serif;
    font-size: 23px;
    letter-spacing: 1px;
    margin-bottom: 10px;
  }
  .contact-title {
    font-family: "Arimo", sans-serif;
    font-style: italic;
    font-size: 16px;
    line-height: 1.3;
  }
  .contact-line {
    font-family: "Arimo", sans-serif;
    font-size: 16px;
    line-height: 1.3;
  }
</style>
</head>
<body>
<main class="canvas">
  <section class="card card-front" aria-label="Card front">
    <span class="brand-dot" aria-hidden="true"></span>
    <h1 class="wordmark">
      <span class="wordmark-main">North Fern</span>
      <span class="wordmark-sub">Holdings</span>
    </h1>
  </section>

  <section class="card card-back" aria-label="Card back">
    <svg class="watermark" viewBox="0 0 440 440" aria-hidden="true">
      <circle cx="220" cy="220" r="220" fill="var(--fern-light)" opacity="0.55"/>
    </svg>
    <div class="contact">
      <p class="contact-name">Marcus Pellington</p>
      <p class="contact-title">Principal</p>
      <p class="contact-line">949-555-0173</p>
      <p class="contact-line">marcus@northfernhq.com</p>
    </div>
  </section>
</main>
</body>
</html>
```